Invitation to Retail Shopping Event

-Must include logo
-Can contain product pictures depending on design
-I prefer any graphics to be my own product pictures
-Should include the following language:
Sip and Shop
Thursday, November 18
11 to 1 pm
487 Birch Lane
Come enjoy sips, snacks and shopping! Be the first to preview our new winter collection and get an early start on your holiday gifting.
Please RSVP to 415-382-9061 or info@brivettenw.com

```html
<!DOCTYPE html>
<html lang="en">
<head>
<meta charset="utf-8">
<title>Brivette NW — Sip and Shop Invitation</title>
<link href="https://fonts.googleapis.com/css2?family=Questrial&family=Montserrat:wght@300&display=swap" rel="stylesheet">
<style>
  :root {
    --backdrop: #ececec;
    --card-dark: #000000;
    --card-light: #474747;
    --ink: #ffffff;
    --blush: #ecd0c8;
    --pattern: #f4f4f4;
    --product-bg: #ffffff;
    --product-tone: #d9c7b4;
  }
  html, body {
    margin: 0;
    width: 1200px;
    height: 1200px;
    overflow: hidden;
    background: var(--backdrop);
  }
  .invitation {
    position: absolute;
    left: 361px;
    top: 240px;
    width: 491px;
    height: 735px;
    background: linear-gradient(to bottom left, var(--card-light) 0%, #262626 45%, var(--card-dark) 100%);
    color: var(--ink);
    font-family: "Questrial", sans-serif;
    overflow: hidden;
  }
  .pattern-corner {
    position: absolute;
    display: block;
  }
  .pattern-corner--top { left: 0; top: 0; }
  .pattern-corner--bottom { right: 0; bottom: 0; }
  .brand-name {
    position: absolute;
    left: 0;
    right: 0;
    top: 150px;
    text-align: center;
    font-family: "Questrial", sans-serif;
    font-size: 42px;
    letter-spacing: 4px;
    color: var(--blush);
    margin: 0;
    font-weight: 400;
  }
  .event-title {
    position: absolute;
    left: 0; right: 0;
    top: 264px;
    margin: 0;
    text-align: center;
    font-size: 38px;
    font-weight: 400;
    letter-spacing: 0.2px;
  }
  .event-details {
    position: absolute;
    left: 0; right: 0;
    top: 323px;
    margin: 0;
    text-align: center;
    font-size: 15.5px;
    line-height: 19.5px;
    font-weight: 400;
  }
  .event-details .address {
    display: block;
    margin-top: 8px;
  }
  .event-blurb {
    position: absolute;
    left: 0; right: 0;
    top: 426px;
    margin: 0;
    text-align: center;
    font-family: "Montserrat", sans-serif;
    font-weight: 300;
    font-size: 16px;
    line-height: 25px;
  }
  .product-row {
    position: absolute;
    left: 0; right: 0;
    top: 528px;
    display: flex;
    justify-content: center;
    gap: 27px;
  }
  .product-spot {
    width: 72px;
    height: 72px;
    border-radius: 50%;
    background: radial-gradient(circle, var(--product-tone) 0%, #eee3da 38%, var(--product-bg) 60%);
  }
  .rsvp {
    position: absolute;
    left: 30px;
    top: 676px;
    margin: 0;
    font-family: "Montserrat", sans-serif;
    font-weight: 300;
    font-size: 12.5px;
    line-height: 17.5px;
  }
</style>
</head>
<body>
  <main class="invitation">
    <svg class="pattern-corner pattern-corner--top" width="215" height="150" viewBox="0 0 215 150" role="img" aria-label="White leopard-spot pattern in the top left corner">
      <path d="M0 0 H213 C170 40 110 60 60 100 C40 118 25 135 12 150 H0 Z" fill="var(--pattern)" opacity="0.9"/>
    </svg>

    <h1 class="brand-name">BRIVETTE NW</h1>

    <h2 class="event-title">Sip and Shop</h2>

    <p class="event-details">
      Thursday, November 18<br>
      11 to 1 pm
      <span class="address">487 Birch Lane</span>
    </p>

    <p class="event-blurb">
      Come enjoy sips, snacks and shopping !<br>
      Be the first to preview our new winter collection<br>
      and get an early start on your holiday gifting.
    </p>

    <div class="product-row">
      <div class="product-spot" role="img" aria-label="Product photo: leopard-print trinket tray"></div>
      <div class="product-spot" role="img" aria-label="Product photo: pink pom-pom slippers"></div>
      <div class="product-spot" role="img" aria-label="Product photo: gold flower stud earrings"></div>
    </div>

    <p class="rsvp">
      Please RSVP to 415-382-9061<br>
      or info@brivettenw.com
    </p>

    <svg class="pattern-corner pattern-corner--bottom" width="215" height="150" viewBox="0 0 215 150" role="img" aria-label="White leopard-spot pattern in the bottom right corner">
      <path d="M215 0 V150 H0 C40 120 100 100 150 60 C175 40 195 20 215 0 Z" fill="var(--pattern)" opacity="0.9"/>
    </svg>
  </main>
</body>
</html>
```